Inspirational Quotes Poster Set

Norbelle is a stylish coworking space, which has a design-oriented vintage look from the 60's with an industrial touch (www.norbelle-example.com) Norbelle Quote Poster Set of 16 posters. The poster should be typo oriented and rather simple. Reflecting a bit the clean billboard design from the sixties. Minimal / simple graphical elements

Target Market(s)

Startups and Entrepreneurs

Industry/Entity Type

Startup

Font styles to use
Sans Serif

Colors

Designer to choose colors to be used in the design.

Requirements
Must have
• Posters need to be on and very stylish

```html
<!DOCTYPE html>
<html lang="en">
<head>
<meta charset="utf-8">
<title>Norbelle Quote Poster Set</title>
<link rel="stylesheet" href="https://fonts.googleapis.com/css2?family=Jost:wght@600&family=Roboto:wght@400&display=swap">
<style>
  :root {
    --ink: #0b0b0b;
    --accent: #9a1b20;
    --stone-light: #fbfbfb;
    --stone-mid: #ececec;
    --stone-vein: #dcdcdc;
  }
  * { margin: 0; padding: 0; box-sizing: border-box; }
  html, body { width: 1200px; height: 847px; overflow: hidden; }
  .poster {
    position: relative;
    width: 1200px;
    height: 847px;
    overflow: hidden;
    background: var(--stone-light);
  }
  .poster__texture {
    position: absolute;
    inset: 0;
    background:
      linear-gradient(125deg, transparent 20%, var(--stone-mid) 30%, transparent 40%),
      linear-gradient(60deg, transparent 55%, var(--stone-vein) 62%, transparent 70%),
      radial-gradient(ellipse at 80% 15%, var(--stone-mid), transparent 60%),
      var(--stone-light);
    opacity: 0.7;
  }
  .quote {
    position: absolute;
    font-family: "Jost", sans-serif;
    font-weight: 600;
    font-size: 71px;
    line-height: 1;
    color: var(--ink);
    letter-spacing: -0.5px;
    white-space: nowrap;
  }
  .quote--first { left: 100px; top: 323px; }
  .quote--second { right: 124px; top: 411px; }
  .attribution {
    position: absolute;
    right: 124px;
    top: 496px;
    font-family: "Roboto", sans-serif;
    font-weight: 400;
    font-size: 33px;
    line-height: 1;
    color: var(--accent);
    white-space: nowrap;
  }
</style>
</head>
<body>
  <main class="poster">
    <div class="poster__texture" role="img" aria-label="White marble texture with soft grey veins"></div>
    <p class="quote quote--first">Ideas are commodity</p>
    <p class="quote quote--second">Execution of them is not</p>
    <p class="attribution">Marcus Hale, Halecorp Chairman and CEO</p>
  </main>
</body>
</html>
```